Gordon Pellbrook Consulting - Web Design Project

We need a web design for my new edgy consulting business specializing in innovation, technology and strategy.

It is our personal goal to turn each client into raving fans by helping them achieve their own business goals and aspirations through assisting them in raising their own innovation and marketing standards.

We provide our personalised and state-of-the-art services to our clients and boards who represent some of the world greatest innovative thinkers.
Updates

Here is some other information which may help shape your thinking.

I've had direct Involvement in the development of the following iPad, iPhone Applications and websites

FarbeyondOzlands.com (TerraLink platform) by Voyage Bureau
http://farbeyondozlands.example.au

Sail Verve by Bright Voyaging
https://apps.example-store.com/au/app/sail-verve/id100000001

uRedlandTR by Travel Territory Board
https://apps.example-store.com/au/app/uredlandtr/id100000002

Wexmoor Trips
http://www.wexmoortrips.example.au

Trek Mapper by Voyage Bureau
http://apps.example-store.com/au/app/trek-mapper/id100000003

Sunward by Sunward Travel Office
https://apps.example-store.com/au/app/sunward/id100000004

Upper Fernridge Valley Route by Visit Coastlands
https://apps.example-store.com/au/app/upper-fernridge-valley-route/id100000005

Wanderer Path by Travel Territory Board and Southern Plains Travel Council
https://apps.example-store.com/au/app/wanderers-path-grand-journey/id100000006

Gordon Pellbrook Consulting (GPC)
November 2012 – Present (8 months)Brisbane, Sydney, Canberra

Gordon’s consults to Small-to-Medium Enterprises (SME) and Government organisations on business strategy, technology strategy, risk mitigation, disruptive technology and innovation in the workplace.

Gordon’s consultancy mantra is that we cannot divorce economic life from cultural life particularly in an era when social capital may be as important as physical capital in business.

Reason: request from designers, I want to see their best efforts

Target Market(s)

35+

Industry/Entity Type

Business

Requirements
Must have
• Please use some of the personal image(s) contained in the zip files which can be downloaded from here

http://filedrop.example/k9Xq2Lm
http://filedrop.example/p4Rt7Vn
http://filedrop.example/z8Hw3Bc
Nice to have
• Black, Sleek design, maybe minimalist. Nice to have a Pixelle for the design. Nice to have it easily ported to Wordpress or be a modified Wordpress template. HTML 5, responsive design

```html
<!DOCTYPE html>
<html lang="en">
<head>
<meta charset="utf-8">
<title>Gordon Pellbrook Consulting</title>
<link href="https://fonts.googleapis.com/css2?family=Source+Sans+3:ital,wght@0,300;0,400;0,600;0,700;1,700&display=swap" rel="stylesheet">
<style>
  :root {
    --bg-top: #5c5c5c;
    --bg-mid: #2f2f2f;
    --bg-bottom: #575757;
    --card: #ffffff;
    --ink: #111111;
    --ink-soft: #6a6a6a;
    --body-text: #555555;
    --nav-bg: #000000;
    --nav-edge: #9a9a9a;
    --nav-text: #ffffff;
    --social-bg: #f3f3f3;
    --social-edge: #c9c9c9;
    --social-text: #555555;
    --photo-light: #e9efe0;
    --photo-mid: #b9c6d4;
    --photo-dark: #7f8fa3;
  }
  html, body {
    margin: 0;
    padding: 0;
    width: 1200px;
    height: 602px;
    overflow: hidden;
  }
  body {
    position: relative;
    font-family: "Source Sans 3", sans-serif;
    background: linear-gradient(to bottom, var(--bg-top) 0%, var(--bg-mid) 48%, var(--bg-bottom) 100%);
  }
  .site-card {
    position: absolute;
    left: 123px;
    top: 78px;
    width: 1004px;
    height: 475px;
    background: var(--card);
    border-top-right-radius: 80px 110px;
    box-shadow: 2px 0 3px rgba(0,0,0,0.35);
  }
  .portrait {
    position: absolute;
    left: 0;
    top: 0;
    width: 320px;
    height: 475px;
    background:
      linear-gradient(to bottom, var(--photo-light) 0%, rgba(233,239,224,0) 45%),
      linear-gradient(to bottom, #dfe6ea 0%, var(--photo-mid) 55%, var(--photo-dark) 100%);
  }
  .intro {
    position: absolute;
    left: 341px;
    top: 190px;
    width: 440px;
  }
  .intro-title {
    margin: 0;
    font-size: 26px;
    font-weight: 700;
    color: var(--ink);
    line-height: 30px;
  }
  .intro-role {
    margin: 0;
    font-size: 24px;
    font-weight: 300;
    color: var(--ink-soft);
    line-height: 30px;
  }
  .intro-text {
    margin: 12px 0 0;
    font-size: 13px;
    line-height: 17px;
    color: var(--body-text);
  }
  .social-links {
    position: absolute;
    left: 339px;
    top: 381px;
    display: flex;
    gap: 8px;
  }
  .social-link {
    height: 30px;
    padding: 0 7px;
    display: flex;
    align-items: center;
    background: var(--social-bg);
    border: 1px solid var(--social-edge);
    border-radius: 3px;
    box-shadow: 0 1px 1px rgba(0,0,0,0.15);
    font-size: 11px;
    font-weight: 600;
    color: var(--social-text);
    text-decoration: none;
  }
  .main-nav {
    position: absolute;
    right: 0;
    top: 199px;
    width: 150px;
  }
  .nav-item {
    display: flex;
    align-items: center;
    height: 40px;
    margin-bottom: 20px;
    background: var(--nav-bg);
    border-bottom: 2px solid var(--nav-edge);
    color: var(--nav-text);
    text-decoration: none;
    font-size: 17px;
    font-weight: 700;
    font-style: italic;
  }
  .nav-item svg {
    width: 26px;
    height: 26px;
    margin-left: 12px;
    flex: none;
  }
  .nav-label {
    flex: 1;
    text-align: center;
    padding-right: 10px;
  }
  .site-footer {
    position: absolute;
    left: 464px;
    top: 570px;
    font-size: 12px;
    color: var(--ink);
  }
</style>
</head>
<body>
  <main class="site-card">
    <div class="portrait" role="img" aria-label="Portrait photograph of Gordon Pellbrook in a grey suit by a bright window"></div>

    <section class="intro">
      <h1 class="intro-title">Gordon Pellbrook Consulting</h1>
      <p class="intro-role">Software Engineer</p>
      <p class="intro-text">Lorem ipsum dolor sit amet, consectetuer adipiscing elit, sed diam nonummy nibh euismod tincidunt ut laoreet dolore magna aliquam erat volutpat. Ut wisi enim ad minim veniam, quis nostrud exerci tation ullamcorper suscipit lobortis nisl ut aliquip ex ea commodo consequat.</p>
    </section>

    <nav class="social-links" aria-label="Social profiles">
      <a class="social-link" href="#">Friendlio</a>
      <a class="social-link" href="#">Chirpy</a>
      <a class="social-link" href="#">Linkwise</a>
      <a class="social-link" href="#">Circlo</a>
    </nav>

    <nav class="main-nav" aria-label="Main">
      <a class="nav-item" href="#">
        <svg viewBox="0 0 26 26" aria-hidden="true"><path d="M3 13 L13 4 L23 13 L20 13 L20 22 L15 22 L15 16 L11 16 L11 22 L6 22 L6 13 Z" fill="#d8d8d8"/></svg>
        <span class="nav-label">Home</span>
      </a>
      <a class="nav-item" href="#">
        <svg viewBox="0 0 26 26" aria-hidden="true"><rect x="5" y="2" width="16" height="22" fill="none" stroke="#fff" stroke-width="2"/><circle cx="13" cy="10" r="3" fill="#fff"/><path d="M8 19 Q13 12 18 19 Z" fill="#fff"/></svg>
        <span class="nav-label">Profile</span>
      </a>
      <a class="nav-item" href="#">
        <svg viewBox="0 0 26 26" aria-hidden="true"><rect x="3" y="8" width="20" height="15" fill="#fff"/><rect x="9" y="4" width="8" height="5" fill="none" stroke="#fff" stroke-width="2"/><rect x="3" y="13" width="20" height="2" fill="#000"/><rect x="11" y="12" width="4" height="4" fill="#fff" stroke="#000" stroke-width="1"/></svg>
        <span class="nav-label">Portfolio</span>
      </a>
      <a class="nav-item" href="#">
        <svg viewBox="0 0 26 26" aria-hidden="true"><rect x="2" y="5" width="22" height="16" rx="2" fill="#fff"/><circle cx="8" cy="11" r="2.5" fill="#000"/><path d="M4 18 Q8 12 12 18 Z" fill="#000"/><rect x="14" y="10" width="7" height="1.6" fill="#000"/><rect x="14" y="14" width="7" height="1.6" fill="#000"/></svg>
        <span class="nav-label">Contact</span>
      </a>
    </nav>
  </main>

  <footer class="site-footer">2012 © Gordon Pellbrook Consulting.com</footer>
</body>
</html>
```